winery and bed & breakfast business card

need a business card design
font and style same as our marketing material
also need something for letterhead

not too colorful, we want professional and simple
name
address
phone number
web site
email
Corvelli Vineyard believes raising a family, living and working passionately with wine on the East End is a privilege. They consider the greatest accolades received over the years have been the thousands of satisfied tasting room visitors. Enlightening visitors to their products and wine region are the most important reasons they continue to make wine on the North Fork
We have created a casual and cozy environment within a rustic historic barn.
An outside seating area nestled among the vines provides visitors with unforgettable sunset views as they enjoy Corvelli’s quality crafted wines.

Target Market(s)

adults over 21

Font styles to use
Serif

Colors
6b449b
ffc214
f78f20
ffffff

Requirements
Must have
• logo
• same font as attached
• logo colors

```html
<!DOCTYPE html>
<html lang="en">
<head>
<meta charset="utf-8">
<title>Corvelli Vineyard – Stationery</title>
<link rel="stylesheet" href="https://fonts.googleapis.com/css2?family=Sorts+Mill+Goudy&family=PT+Sans&display=swap">
<style>
  :root {
    --purple: #4a3358;
    --grape: #6b449b;
    --orange: #f78f20;
    --gold: #ffc214;
    --ink: #222222;
    --rule: #8a8a8a;
    --stage: #ececec;
    --paper: #ffffff;
    --edge: #e2e2e2;
    --label: #1a1a1a;
  }
  * { margin: 0; padding: 0; box-sizing: border-box; }
  html, body { width: 1200px; height: 1084px; overflow: hidden; background: var(--paper); }
  body { position: relative; font-family: "Sorts Mill Goudy", Georgia, serif; color: var(--ink); }

  .section-label {
    position: absolute;
    font-family: "PT Sans", Arial, sans-serif;
    font-size: 18px;
    color: var(--label);
    letter-spacing: 0.2px;
  }
  .section-label--preview { left: 877px; top: 304px; }
  .section-label--letterhead { left: 734px; top: 675px; }
  .section-label--card { left: 736px; top: 814px; }

  /* Preview: flat letterhead */
  .preview { position: absolute; left: 25px; top: 21px; width: 814px; height: 640px; background: var(--stage); }
  .letterhead {
    position: absolute; left: 183px; top: 24px; width: 448px; height: 592px;
    background: var(--paper); border: 1px solid var(--edge);
  }
  .letterhead__brand { position: absolute; left: 0; right: 0; top: 30px; text-align: center; }
  .brand-dot { display: block; margin: 0 auto 6px; border-radius: 50%; background: var(--orange); }
  .letterhead .brand-dot { width: 26px; height: 26px; }
  .brand-name { color: var(--purple); letter-spacing: 3px; line-height: 1.1; }
  .letterhead .brand-name { font-size: 11px; }
  .letterhead .brand-name small { font-size: 6px; letter-spacing: 1.5px; display: block; }
  .letterhead__art { display: block; margin: 3px auto 0; width: 40px; height: 20px; }
  .letterhead__rule { position: absolute; left: 130px; right: 130px; top: 122px; height: 1px; background: var(--rule); }
  .letterhead__site { position: absolute; left: 0; right: 0; top: 128px; text-align: center; font-size: 7px; letter-spacing: 1px; }
  .letterhead__footer {
    position: absolute; left: 0; right: 0; bottom: 34px; text-align: center;
    font-size: 8px; letter-spacing: 1.4px;
  }
  .letterhead__footer span { margin: 0 8px; }

  /* Business card front */
  .card-front {
    position: absolute; left: 33px; top: 824px; width: 397px; height: 238px;
    background: var(--paper); border: 1px solid #efefef;
  }
  .card-front__brand { position: absolute; left: 0; right: 0; top: 28px; text-align: center; }
  .card-front .brand-dot { width: 66px; height: 66px; }
  .card-front .brand-name { font-size: 22px; letter-spacing: 5px; margin-top: 6px; }
  .card-front .brand-name small { display: block; font-size: 10px; letter-spacing: 2px; }
  .card-front__art { position: absolute; left: 166px; top: 142px; width: 80px; height: 50px; }
  .card-front__rule { position: absolute; left: 0; right: 0; top: 179px; height: 1px; background: var(--rule); }
  .card-front__site { position: absolute; left: 0; right: 0; top: 199px; text-align: center; font-size: 12px; letter-spacing: 2.2px; }

  /* Business card rear */
  .card-rear { position: absolute; left: 503px; top: 866px; width: 320px; }
  .card-rear__name { font-size: 18px; letter-spacing: 0.5px; color: var(--ink); }
  .card-rear__list { list-style: none; margin-top: 48px; font-size: 12px; letter-spacing: 2.2px; }
  .card-rear__list li { display: flex; align-items: center; height: 22px; }
  .card-rear__list li.gap { margin-top: 4px; }
  .card-rear__list svg { width: 14px; height: 14px; margin-right: 8px; flex: none; }
</style>
</head>
<body>

  <div class="section-label section-label--preview">PREVIEW</div>
  <div class="section-label section-label--letterhead">LETTERHEAD WITH ADDRESS OR CONTACT</div>
  <div class="section-label section-label--card">BUSINESS CARD FRONT AND REAR</div>

  <section class="preview">
    <div class="letterhead">
      <div class="letterhead__brand">
        <span class="brand-dot"></span>
        <div class="brand-name">CORVELLI<small>VINEYARD</small></div>
        <svg class="letterhead__art" role="img" aria-label="Grape cluster and vine leaf illustration" viewBox="0 0 40 20">
          <defs><linearGradient id="vine-a" x1="0" x2="1"><stop offset="0" stop-color="#f7a94a"/><stop offset="1" stop-color="#8a6bb4"/></linearGradient></defs>
          <rect width="40" height="20" rx="6" fill="url(#vine-a)"/>
        </svg>
      </div>
      <div class="letterhead__rule"></div>
      <div class="letterhead__site">www.corvellivineyard.com</div>
      <div class="letterhead__footer">
        <span>210 Orchard Lane • Harborview • NY 10000</span><span>555-014-2760</span><span>info@corvellivineyard.com</span>
      </div>
    </div>
  </section>

  <section class="card-front">
    <div class="card-front__brand">
      <span class="brand-dot"></span>
      <div class="brand-name">CORVELLI<small>VINEYARD</small></div>
    </div>
    <svg class="card-front__art" role="img" aria-label="Grape cluster and vine leaf illustration" viewBox="0 0 80 50">
      <defs><linearGradient id="vine-b" x1="0" x2="1"><stop offset="0" stop-color="#f7a94a"/><stop offset="0.5" stop-color="#a689c9"/><stop offset="1" stop-color="#f7a94a"/></linearGradient></defs>
      <rect width="80" height="50" rx="18" fill="url(#vine-b)"/>
    </svg>
    <div class="card-front__rule"></div>
    <div class="card-front__site">www.corvellivineyard.com</div>
  </section>

  <section class="card-rear">
    <div class="card-rear__name">CORVELLI</div>
    <ul class="card-rear__list">
      <li>www.corvellivineyard.com</li>
      <li>210 Orchard Lane • Harborview • NY 10000</li>
      <li class="gap">
        <svg viewBox="0 0 14 14" aria-hidden="true"><path d="M2 5c0-2 2-3 5-3s5 1 5 3l-2 1-1-2H5L4 6z" fill="#222"/><rect x="3" y="7" width="8" height="5" rx="1" fill="#222"/><circle cx="7" cy="9.5" r="1.3" fill="#fff"/></svg>
        555-014-2760
      </li>
      <li class="gap">
        <svg viewBox="0 0 14 14" aria-hidden="true"><rect x="1.5" y="3" width="11" height="9" fill="none" stroke="#222" stroke-width="1.3"/><path d="M1.5 3l5.5 5 5.5-5" fill="none" stroke="#222" stroke-width="1.3"/></svg>
        info@corvellivineyard.com
      </li>
    </ul>
  </section>

</body>
</html>
```